PowerPoint Design Project

Kestrel Estate Group is a Melbourne based property development management company. We provide a comprehensive range of development management services to a select group of listed developers, private landowners, overseas investors and development partners and institutional clients. Our website provides additional information about the company:
http://www.kestreleg.com.au
We are looking for a versatile powerpoint design that can be used across a wide variety of presentations including; pitch documents, client reports, Information memorandums, and downloadable credential packs etc. We have attached a good example document.
Updates

Industry/Entity Type

It Company

Requirements
Must have
• The design should have the following slides as a minimum: Intro Page, transition slides, profile slides, slides for graphics,

```html
<!DOCTYPE html>
<html lang="en">
<head>
<meta charset="UTF-8">
<title>Kestrel Estate Group – Project Title</title>
<link rel="stylesheet" href="https://fonts.googleapis.com/css2?family=Roboto+Condensed:wght@700&family=Open+Sans:wght@400;600;700&display=swap">
<style>
  :root {
    --blue-deep: #123f86;
    --blue-mid: #1a56a8;
    --blue-light: #2a6fc4;
    --rule-dark: #1e1220;
    --title-blue: #1f4f9e;
    --title-black: #111111;
    --text-grey: #5a5a5a;
    --footer-blue: #1a4a8c;
    --white: #ffffff;
  }
  * { margin: 0; padding: 0; box-sizing: border-box; }
  html, body { width: 1200px; height: 900px; overflow: hidden; background: var(--white); }
  .slide {
    position: relative;
    width: 1200px;
    height: 900px;
    overflow: hidden;
    background: var(--white);
    font-family: "Open Sans", Arial, sans-serif;
  }
  .hero-band {
    position: absolute;
    left: 0; top: 0;
    width: 1200px; height: 461px;
    background: linear-gradient(180deg, var(--blue-mid) 0%, var(--blue-deep) 100%);
  }
  .hero-photo {
    position: absolute;
    left: 0; top: 0;
    width: 300px; height: 461px;
    background:
      linear-gradient(90deg, rgba(26,86,168,0) 55%, var(--blue-mid) 100%),
      linear-gradient(180deg, #3d8fe0 0%, #1f6dc9 45%, #1a5bb2 100%);
  }
  .hero-rule {
    position: absolute;
    left: 0; top: 459px;
    width: 1200px; height: 5px;
    background: var(--rule-dark);
  }
  .brand-name {
    position: absolute;
    right: 27px; top: 398px;
    font-family: "Open Sans", Arial, sans-serif;
    font-weight: 700;
    font-size: 32px;
    letter-spacing: 1px;
    color: var(--white);
    white-space: nowrap;
  }
  .content-shade {
    position: absolute;
    left: 540px; top: 464px;
    width: 660px; height: 300px;
    background: radial-gradient(ellipse at 40% 20%, rgba(200,205,212,0.35) 0%, rgba(255,255,255,0) 65%);
  }
  .title-block {
    position: absolute;
    right: 23px; top: 494px;
    text-align: right;
  }
  .project-title {
    font-family: "Roboto Condensed", "Arial Narrow", sans-serif;
    font-weight: 700;
    font-size: 46px;
    line-height: 1.1;
    color: var(--title-black);
  }
  .project-title .accent { color: var(--title-blue); }
  .project-date {
    margin-top: 14px;
    font-weight: 600;
    font-size: 22px;
    color: var(--text-grey);
  }
  .project-summary {
    margin-top: 22px;
    font-weight: 400;
    font-size: 20px;
    line-height: 33px;
    color: var(--text-grey);
  }
  .footer-band {
    position: absolute;
    left: 0; bottom: 0;
    width: 1200px; height: 40px;
    background: var(--footer-blue);
  }
  .copyright {
    position: absolute;
    right: 27px; top: 9px;
    font-size: 17px;
    color: var(--white);
  }
</style>
</head>
<body>
  <main class="slide">
    <section class="hero-band">
      <div class="hero-photo" role="img" aria-label="Photograph of a glass office tower facade glowing blue"></div>
      <div class="brand-name">KESTREL ESTATE GROUP</div>
    </section>
    <div class="hero-rule"></div>

    <div class="content-shade" role="img" aria-label="Soft grey halftone texture behind the title"></div>

    <section class="title-block">
      <h1 class="project-title"><span class="accent">Project</span> Title Here</h1>
      <p class="project-date">Date : 01 - 01 - 2013</p>
      <p class="project-summary">
        Sub text here Sub text here Sub text here Sub text here<br>
        Sub text here Sub text here Sub text here Sub
      </p>
    </section>

    <footer class="footer-band">
      <p class="copyright">Copyright Text Here</p>
    </footer>
  </main>
</body>
</html>
```